Packaging design for a revolutionary hi-protein snack of Norwegian salmon

We need a breathtaking packing design for a smal snack bag (30 g) for a revolutionary new hi-protein snack made of Norwegian salmon. The product will be made with two different flavors; MANGO and WASABI. The product is extreme high in protein (60%) and omega 3, and are just natural.

We want to see a bold and fresh design that appeals to protein lovers of all ages.

Target Market(s)

Our target market is boys and girls that are 18-35 years old and that are interested in working out and eating healthy.

Industry/Entity Type

Snack industry (functional food, healthy snack, protein snack)

Font styles to use
Sans Serif

Requirements
Must have
• The package design must give the customer a WOW feeling. "HI-PROTEIN SNACK" must be highligted. Further, the design must use the Tidal Compass setup (attached).

```html
<!DOCTYPE html>
<html lang="en">
<head>
<meta charset="utf-8">
<title>Hi Protein Snack – Pack Range</title>
<link rel="stylesheet" href="https://fonts.googleapis.com/css2?family=Fredoka:wght@600;700&family=Oswald:wght@500&family=Quicksand:wght@500&family=Cinzel:wght@500&family=Open+Sans:ital,wght@1,600;1,800&display=swap">
<style>
  :root {
    --stage: #141414;
    --red-deep: #7c1a12;
    --red-main: #b8321c;
    --red-glow: #e0561e;
    --green-deep: #13501c;
    --green-main: #23812d;
    --green-glow: #35a23c;
    --hi-red: #f0282c;
    --brand-green: #1d8a25;
    --ink-dark: #17331c;
    --white: #ffffff;
    --band-red: #d7261f;
    --badge-green: #17e24a;
    --snack-orange: #e9731f;
    --snack-amber: #f4a23a;
  }
  * { box-sizing: border-box; margin: 0; padding: 0; }
  html, body { width: 1200px; height: 933px; overflow: hidden; background: var(--stage); }
  .range { position: relative; width: 1200px; height: 933px; }

  .pack {
    position: absolute; top: 134px; width: 437px; height: 706px; overflow: hidden;
    background: radial-gradient(ellipse at 55% 42%, var(--glow) 0%, var(--main) 45%, var(--deep) 100%);
  }
  .pack--mango { left: 137px; --glow: var(--red-glow); --main: var(--red-main); --deep: var(--red-deep); }
  .pack--wasabi { left: 682px; --glow: var(--green-glow); --main: var(--green-main); --deep: var(--green-deep); }

  .pack__seal {
    position: absolute; left: 0; width: 100%;
    background: repeating-linear-gradient(0deg, rgba(0,0,0,.22) 0 2px, rgba(255,255,255,.06) 2px 5px), var(--deep);
  }
  .pack__seal--top { top: 0; height: 77px; }
  .pack__seal--bottom { bottom: 0; height: 30px; }
  .pack__hang-hole {
    position: absolute; left: 173px; top: 33px; width: 94px; height: 16px;
    border-radius: 8px; background: var(--stage);
  }

  .snack-photo {
    position: absolute; border-radius: 30% 40% 35% 45%;
    background: radial-gradient(circle at 50% 45%, var(--snack-amber), var(--snack-orange) 60%, rgba(200,80,20,.6) 100%);
  }
  .snack-photo--hero { left: 91px; top: 429px; width: 252px; height: 206px; }
  .snack-photo--corner-right { left: 338px; top: 127px; width: 77px; height: 71px; }
  .snack-photo--corner-left { left: -10px; top: 69px; width: 48px; height: 71px; }

  .brand {
    position: absolute; left: 34px; top: 150px; width: 110px;
    font-family: "Fredoka", sans-serif; font-weight: 700; font-size: 24px; line-height: 1;
    color: var(--brand-green); text-align: center; transform: none;
  }

  .headline { position: absolute; left: 0; width: 458px; text-align: center; }
  .headline--hi {
    top: 140px; font-family: "Fredoka", sans-serif; font-weight: 700; font-size: 96px; line-height: 1;
    color: var(--hi-red); -webkit-text-stroke: 8px var(--white); paint-order: stroke fill;
  }
  .headline--protein {
    top: 226px; font-family: "Fredoka", sans-serif; font-weight: 700; font-size: 76px; line-height: 1; letter-spacing: -1px;
    color: var(--protein-fill); -webkit-text-stroke: 8px var(--white); paint-order: stroke fill;
  }
  .pack--mango { --protein-fill: var(--brand-green); --flavor-fill: var(--hi-red); }
  .pack--wasabi { --protein-fill: var(--ink-dark); --flavor-fill: var(--ink-dark); }
  .headline--snack {
    top: 298px; left: 6px; font-family: "Oswald", sans-serif; font-weight: 500; font-size: 36px; line-height: 1;
    color: var(--hi-red); -webkit-text-stroke: 4px var(--white); paint-order: stroke fill; transform: scaleX(.9);
  }
  .flavor {
    position: absolute; left: 0; top: 344px; width: 460px; text-align: center;
    font-family: "Quicksand", sans-serif; font-weight: 500; font-size: 50px; line-height: 1; white-space: nowrap;
    color: var(--flavor-fill); -webkit-text-stroke: 4px var(--white); paint-order: stroke fill;
  }

  .claim-band {
    position: absolute; left: 7px; top: 637px; width: 353px; height: 39px;
    background: var(--band-red); border-top: 3px solid var(--claim-edge);
    font-family: "Cinzel", serif; font-weight: 500; font-size: 18px; color: var(--white);
    line-height: 34px; padding-left: 8px; white-space: nowrap;
  }
  .pack--mango { --claim-edge: var(--badge-green); --badge: var(--badge-green); }
  .pack--wasabi { --claim-edge: var(--band-red); --badge: var(--band-red); }

  .net-weight {
    position: absolute; left: 364px; top: 626px; width: 59px; height: 75px;
    background: var(--badge); text-align: center; font-family: "Open Sans", sans-serif; color: #111;
  }
  .net-weight__label { display: block; margin-top: 8px; font-style: italic; font-weight: 600; font-size: 8.5px; line-height: 1.35; }
  .net-weight__value { display: block; margin-top: 6px; font-style: italic; font-weight: 800; font-size: 24px; line-height: 1; }
</style>
</head>
<body>
<main class="range">

  <section class="pack pack--mango" aria-label="Mango flavor pack">
    <div class="pack__seal pack__seal--top"></div>
    <div class="pack__hang-hole"></div>
    <div class="snack-photo snack-photo--corner-left" role="img" aria-label="Dried salmon snack piece"></div>
    <div class="snack-photo snack-photo--corner-right" role="img" aria-label="Dried salmon snack piece"></div>
    <p class="brand">Tidal Compass</p>
    <h1 class="headline headline--hi">HI</h1>
    <p class="headline headline--protein">PROTEIN</p>
    <p class="headline headline--snack">SNACK</p>
    <p class="flavor">Mango flavor</p>
    <div class="snack-photo snack-photo--hero" role="img" aria-label="Pile of mango-glazed dried salmon snack pieces"></div>
    <p class="claim-band">PROTEIN (60%) AND OMEGA 3,</p>
    <div class="pack__seal pack__seal--bottom"></div>
    <div class="net-weight"><span class="net-weight__label">NET<br>WEIGHT</span><span class="net-weight__value">30g</span></div>
  </section>

  <section class="pack pack--wasabi" aria-label="Mango Wasabi pack">
    <div class="pack__seal pack__seal--top"></div>
    <div class="pack__hang-hole"></div>
    <div class="snack-photo snack-photo--corner-left" role="img" aria-label="Dried salmon snack piece"></div>
    <div class="snack-photo snack-photo--corner-right" role="img" aria-label="Dried salmon snack piece"></div>
    <p class="brand">Tidal Compass</p>
    <h1 class="headline headline--hi">HI</h1>
    <p class="headline headline--protein">PROTEIN</p>
    <p class="headline headline--snack">SNACK</p>
    <p class="flavor">Mango&nbsp; Wasabi</p>
    <div class="snack-photo snack-photo--hero" role="img" aria-label="Pile of mango wasabi dried salmon snack pieces"></div>
    <p class="claim-band">PROTEIN (60%) AND OMEGA 3,</p>
    <div class="pack__seal pack__seal--bottom"></div>
    <div class="net-weight"><span class="net-weight__label">NET<br>WEIGHT</span><span class="net-weight__value">30g</span></div>
  </section>

</main>
</body>
</html>
```